Social Media Post Quote #3 - Native American Organization

- RADIANT - must be included
- Protect your community. Protect Your Elders. Stay Vaccinated. must be included
- Attached, company Logo, campaign logos and sample flu social media image. - our audience likes BRIGHT colors.
- Must include image from the United States, representing Land/Nature from one of the following regions, Plains and Woodlands, or Southwest, or Mountains, or Coast.
- must include quote: The well-being of our community’s mind, body, and spirit is sacred.
- One image will be provided three times - incorporating campaign logos - in some fashion
- For inspiration - https://velmoranth.org/ and https://www.kindrelay.net/Velmoranth

```html
<!DOCTYPE html>
<html lang="en">
<head>
<meta charset="utf-8">
<title>Velmoranth – Protect your Elders</title>
<link rel="stylesheet" href="https://fonts.googleapis.com/css2?family=Oswald:wght@400;500;600;700&display=swap">
<style>
  :root {
    --teal: #3ea6b5;
    --teal-deep: #2f97a7;
    --clay: #b4524a;
    --paper: #ecebe3;
    --white: #ffffff;
    --sky: #cfe2ee;
    --tundra: #b8532e;
  }
  * { margin: 0; padding: 0; box-sizing: border-box; }
  html, body {
    width: 1200px;
    height: 1200px;
    overflow: hidden;
    background: var(--paper);
  }
  .post {
    position: relative;
    width: 1200px;
    height: 1200px;
    background: var(--paper);
    font-family: "Oswald", "Arial Narrow", sans-serif;
    overflow: hidden;
  }
  .border-band {
    position: absolute;
    left: 0;
    width: 1200px;
    height: 32px;
    background: linear-gradient(180deg, var(--teal) 0%, var(--teal) 45%, var(--clay) 55%, var(--clay) 100%);
    opacity: 0.55;
  }
  .border-band--top { top: 0; }
  .border-band--bottom { bottom: 0; }

  .intro-panel {
    position: absolute;
    left: 0;
    top: 32px;
    width: 642px;
    height: 1136px;
    text-align: center;
  }
  .brand {
    position: absolute;
    top: 150px;
    left: 0;
    width: 642px;
    display: flex;
    justify-content: center;
    align-items: center;
    gap: 18px;
  }
  .brand__mark {
    width: 34px;
    height: 34px;
    background: var(--teal);
  }
  .brand__name {
    color: var(--teal);
    font-weight: 600;
    font-size: 92px;
    line-height: 1;
    letter-spacing: 1px;
  }
  .org-name {
    position: absolute;
    top: 370px;
    left: 0;
    width: 642px;
    line-height: 1;
  }
  .org-name__line1 {
    display: block;
    color: var(--teal);
    font-weight: 500;
    font-size: 27px;
    letter-spacing: 0.5px;
  }
  .org-name__line2 {
    display: block;
    margin-top: 8px;
    color: var(--clay);
    font-weight: 600;
    font-size: 44px;
    letter-spacing: 0.5px;
  }
  .quote {
    position: absolute;
    top: 508px;
    left: 0;
    width: 642px;
    color: var(--teal);
    font-weight: 600;
    font-size: 66px;
    line-height: 78px;
  }
  .quote__accent { color: var(--clay); }
  .campaign-name {
    position: absolute;
    top: 972px;
    left: 0;
    width: 642px;
    color: var(--clay);
    font-weight: 600;
    font-size: 46px;
    line-height: 1;
    letter-spacing: 2px;
  }

  .landscape {
    position: absolute;
    left: 642px;
    top: 32px;
    width: 558px;
    height: 1136px;
    background: linear-gradient(180deg,
      #cde1ee 0%, #d6e6ef 18%,
      #f2f3f5 24%, #e4e6ec 32%,
      #9d93ad 40%, #7f7690 46%,
      #b0794f 52%, #8f5a3c 58%,
      #6e6a4c 66%, #5b6a45 72%,
      #b2582e 80%, #c06a32 90%, #a2482a 100%);
  }
  .call-to-action {
    position: absolute;
    left: 690px;
    top: 912px;
    color: var(--white);
    font-weight: 600;
    font-size: 40px;
    line-height: 58px;
  }
  .call-to-action__line { display: block; }
  .call-to-action__highlight {
    display: inline-block;
    margin-top: 6px;
    padding: 0 12px;
    background: var(--teal-deep);
    line-height: 62px;
  }
</style>
</head>
<body>
  <main class="post">
    <div class="border-band border-band--top" role="img" aria-label="Woven zigzag border pattern in teal and clay red"></div>

    <section class="intro-panel">
      <div class="brand">
        <span class="brand__mark" aria-hidden="true"></span>
        <span class="brand__name">Velmoranth</span>
      </div>
      <p class="org-name">
        <span class="org-name__line1">VELMORANTH ALLIANCE FOR</span>
        <span class="org-name__line2">ELDER WELLNESS</span>
      </p>
      <p class="quote">
        The well-being of<br>
        our community’s<br>
        mind, body, and<br>
        spirit is <span class="quote__accent">sacred</span>.
      </p>
      <p class="campaign-name">RADIANT</p>
    </section>

    <div class="landscape" role="img" aria-label="Photograph of snow-capped mountains above rolling autumn tundra in red and orange tones"></div>

    <p class="call-to-action">
      <span class="call-to-action__line">Protect your Community.</span>
      <span class="call-to-action__line">Protect your Elders.</span>
      <span class="call-to-action__highlight">Stay vaccinated.</span>
    </p>

    <div class="border-band border-band--bottom" role="img" aria-label="Woven zigzag border pattern in teal and clay red"></div>
  </main>
</body>
</html>
```